Consumer and commercial IOT solutions (Internet Of Things)

We are a startup and are looking for business cards with logo. The logo will appear on all of our media as well as our ecommerce site and social sites that have yet to be developed. We want to present a fresh face on a high tech company that innovates at every turn. You can read about our solutions on our information only web site www.plorbaxsystems.net - We have some wording we would like used on our business cards but there is no place for this except for here. The company name is "Plorbax Systems" I have some samples of logos I am interested in seeing but I will let your team make the initial presentations

```html
<!DOCTYPE html>
<html lang="en">
<head>
<meta charset="utf-8">
<title>Plorbax Systems – Business Card</title>
<link href="https://fonts.googleapis.com/css2?family=Arimo:wght@400;700&display=swap" rel="stylesheet">
<style>
  :root {
    --page-bg: #2a2a2c;
    --card-bg: #1d1e20;
    --accent: #f26a25;
    --text-light: #eef0ee;
    --rule: #55585a;
  }
  * { box-sizing: border-box; margin: 0; padding: 0; }
  html, body { width: 1200px; height: 1108px; overflow: hidden; }
  body {
    background: var(--page-bg);
    font-family: "Arimo", Arial, sans-serif;
    position: relative;
  }
  .card {
    position: absolute;
    top: 214px;
    width: 400px;
    height: 680px;
    background: var(--card-bg);
    border-radius: 22px;
    box-shadow: 0 14px 40px rgba(0,0,0,.45);
    overflow: hidden;
  }
  .card--front { left: 150px; }
  .card--back { left: 650px; }

  .brand {
    position: absolute;
    top: 110px;
    left: 0; right: 0;
    display: flex;
    flex-direction: column;
    align-items: center;
    gap: 30px;
  }
  .brand__mark {
    width: 64px; height: 64px;
    border: 6px solid var(--accent);
    border-radius: 50%;
  }
  .brand__name {
    color: var(--text-light);
    font-size: 32px;
    font-weight: 400;
    letter-spacing: .5px;
    white-space: nowrap;
  }

  .person {
    position: absolute;
    top: 360px;
    left: 0; right: 0;
    text-align: center;
  }
  .person__name {
    color: var(--accent);
    font-size: 27px;
    letter-spacing: .5px;
  }
  .person__title {
    color: var(--text-light);
    font-size: 19px;
    margin-top: 4px;
  }

  .contact-icons {
    position: absolute;
    top: 452px;
    left: 60px; right: 60px;
    display: flex;
    align-items: center;
    gap: 8px;
  }
  .contact-icons .rule { flex: 1; height: 1px; background: var(--rule); }
  .icon {
    width: 32px; height: 32px;
    background: var(--accent);
    border-radius: 5px;
    display: flex; align-items: center; justify-content: center;
  }
  .icon svg { width: 20px; height: 20px; }

  .contact {
    position: absolute;
    top: 500px;
    left: 0; right: 0;
    text-align: center;
    color: var(--text-light);
    font-size: 19px;
    line-height: 28px;
  }
  .contact__rule {
    width: 230px; height: 1px;
    background: var(--rule);
    margin: 10px auto;
  }

  .back-pattern {
    position: absolute;
    inset: 0;
    background: radial-gradient(circle at 75% 20%, #3a3b3d 0%, #222325 45%, #18191a 100%);
  }
  .back-brand {
    position: absolute;
    left: 0; right: 0;
    top: 470px;
    display: flex;
    flex-direction: column;
    align-items: center;
    gap: 10px;
  }
  .back-brand__mark {
    width: 42px; height: 42px;
    border: 5px solid var(--accent);
    border-radius: 50%;
  }
  .back-brand__name {
    color: var(--text-light);
    font-size: 16px;
    letter-spacing: .5px;
  }
</style>
</head>
<body>
  <section class="card card--front">
    <div class="brand">
      <span class="brand__mark"></span>
      <div class="brand__name">Plorbax Systems</div>
    </div>

    <div class="person">
      <div class="person__name">DANIEL MARSH</div>
      <div class="person__title">Managing Director</div>
    </div>

    <div class="contact-icons">
      <span class="rule"></span>
      <span class="icon" aria-label="Phone">
        <svg viewBox="0 0 24 24" fill="none" stroke="#1d1e20" stroke-width="2.2" stroke-linecap="round" stroke-linejoin="round"><path d="M5 4h4l2 5-2.5 1.5a11 11 0 0 0 5 5L15 13l5 2v4a2 2 0 0 1-2 2A16 16 0 0 1 3 6a2 2 0 0 1 2-2"/></svg>
      </span>
      <span class="icon" aria-label="Email">
        <svg viewBox="0 0 24 24" fill="none" stroke="#1d1e20" stroke-width="2.2" stroke-linejoin="round"><rect x="3" y="6" width="18" height="12" rx="1"/><path d="M3 7l9 7 9-7"/></svg>
      </span>
      <span class="icon" aria-label="Website">
        <svg viewBox="0 0 24 24" fill="none" stroke="#1d1e20" stroke-width="2.2"><circle cx="12" cy="12" r="9"/><path d="M3 12h18M12 3c3 3 3 15 0 18M12 3c-3 3-3 15 0 18"/></svg>
      </span>
      <span class="rule"></span>
    </div>

    <div class="contact">
      <div>044-987 654 321</div>
      <div>info@plorbaxsystems.net</div>
      <div>www.plorbaxsystems.net</div>
      <div class="contact__rule"></div>
      <div>87, Harbor Lane</div>
      <div>45320,Northland</div>
    </div>
  </section>

  <section class="card card--back">
    <div class="back-pattern" role="img" aria-label="Repeating glossy spot-varnish pattern on a black background"></div>
    <div class="back-brand">
      <span class="back-brand__mark"></span>
      <span class="back-brand__name">Plorbax Systems</span>
    </div>
  </section>
</body>
</html>
```